Marlow Hire Business Card for recruitment company

We are looking for a Business Card Design that incorporates our personal details and our busines name and logo. We are a specialized search consultancy that recruit Property and Construction professionals.
We would like a business card that stands out and is appealing to the Construction and Property industry as well.

Target Market(s)

people in the construction and property industry

Contact Information for Business Card

Business Name and logo

Font styles to use
Serif

Colors
0094D4
00A9DD
6FCCEA
C7EBF8
E9F6FB

Requirements
Must have
• Business name and logo as well as contact details
Should not have
• No photos of us please

```html
<!DOCTYPE html>
<html lang="en">
<head>
<meta charset="utf-8">
<title>Marlow Hire – Business Card</title>
<link href="https://fonts.googleapis.com/css2?family=Source+Sans+3:wght@300;400&display=swap" rel="stylesheet">
<style>
  :root {
    --backdrop: #c9c9c9;
    --paper: #ffffff;
    --ink-deep: #0b3c4e;
    --ink-soft: #7f9ba7;
    --brand-teal: #003e51;
    --brand-mist: #8ba7b1;
  }
  * { margin: 0; padding: 0; box-sizing: border-box; }
  html, body {
    width: 1200px;
    height: 1000px;
    overflow: hidden;
    background: var(--backdrop);
    font-family: "Source Sans 3", "Source Sans Pro", sans-serif;
  }
  .canvas { position: relative; width: 1200px; height: 1000px; }

  .card {
    position: absolute;
    width: 628px;
    height: 377px;
  }

  /* Front side */
  .card-front {
    left: 94px;
    top: 103px;
    background: var(--paper);
  }
  .holder-name {
    position: absolute;
    left: 36px;
    top: 103px;
    font-size: 38px;
    font-weight: 400;
    color: var(--ink-deep);
    line-height: 1;
  }
  .holder-role {
    position: absolute;
    left: 37px;
    top: 150px;
    font-size: 16px;
    font-weight: 400;
    color: var(--ink-soft);
    line-height: 1;
  }
  .contact-list {
    position: absolute;
    left: 38px;
    top: 238px;
    list-style: none;
  }
  .contact-item {
    display: flex;
    align-items: center;
    height: 33px;
    font-size: 21px;
    font-weight: 400;
    color: var(--ink-soft);
  }
  .contact-icon {
    width: 20px;
    height: 20px;
    margin-right: 9px;
    fill: var(--ink-deep);
    flex: none;
  }

  /* Back side */
  .card-back {
    left: 473px;
    top: 508px;
    width: 629px;
    height: 378px;
    background: var(--brand-teal);
  }
  .brand-name {
    position: absolute;
    left: 0;
    right: 0;
    top: 164px;
    text-align: center;
    font-size: 54px;
    font-weight: 300;
    letter-spacing: 2px;
    color: var(--brand-mist);
    line-height: 1;
  }
  .brand-web {
    position: absolute;
    left: 0;
    right: 0;
    top: 312px;
    text-align: center;
    font-size: 16px;
    font-weight: 400;
    color: var(--brand-mist);
  }
</style>
</head>
<body>
<main class="canvas">

  <section class="card card-front" aria-label="Business card front">
    <h1 class="holder-name">Clara Whitfield</h1>
    <p class="holder-role">Director | Senior Search Consultant</p>
    <ul class="contact-list">
      <li class="contact-item">
        <svg class="contact-icon" viewBox="0 0 24 24" aria-hidden="true"><path d="M6.6 10.8a15.1 15.1 0 0 0 6.6 6.6l2.2-2.2c.3-.3.7-.4 1-.2 1.1.4 2.3.6 3.6.6.6 0 1 .4 1 1V20c0 .6-.4 1-1 1A17 17 0 0 1 3 4c0-.6.4-1 1-1h3.5c.6 0 1 .4 1 1 0 1.3.2 2.5.6 3.6.1.3 0 .7-.2 1z"/></svg>
        <span>+64 27 000 4821</span>
      </li>
      <li class="contact-item">
        <svg class="contact-icon" viewBox="0 0 24 24" aria-hidden="true"><path d="M2 6h20v12H2z M2 6l10 7 10-7" fill="var(--ink-deep)" stroke="#fff" stroke-width="1.4"/></svg>
        <span>clara@marlowhire.nz</span>
      </li>
      <li class="contact-item">
        <svg class="contact-icon" viewBox="0 0 24 24" aria-hidden="true"><path d="M12 2a7 7 0 0 0-7 7c0 5.2 7 13 7 13s7-7.8 7-13a7 7 0 0 0-7-7zm0 9.5a2.5 2.5 0 1 1 0-5 2.5 2.5 0 0 1 0 5z"/></svg>
        <span>Auckland, New Zealand</span>
      </li>
    </ul>
  </section>

  <section class="card card-back" aria-label="Business card back">
    <p class="brand-name">MARLOW HIRE</p>
    <p class="brand-web">www.marlowhire.nz</p>
  </section>

</main>
</body>
</html>
```